Merrivale construction website for a high end luxury custom home builder

I need a website designed for a high end luxury custom home builder. I would like the website to host a number activities. A blog/vlog on the page where I can post about the projects being built how to's what to look out for during the build, A designated testimonial page but also having testimonials posted on the other pages like the gallery linked to the photos of the completed projects. a gallery page, an about us page, services page that demonstrate what we do and what we are capable of, and hopefully when I start winning awards, and awards page.
Home page
about us page
services page
gallery
testimonial
awards page but I my need to add that later.
I already have the domain name for the website. www.merrivaleconstruction.com.au
I recently completed a sketch hive page for my logo and will post the logo documents below.

Target Market(s)

I'd like to target professions with cash enough to build a house. I would like peolpe to understand that they are buy a price when they are getting quote to build there house. It seems like people just look for the cheapest price and end up with an inferior product. Where as people need to understand that a builder with the high price ( not astronomically higher 15-20% higher) are the ones with correct systems in place, a bide by correct OHS and use proper and correct product. If that can be conveyed through the website somehow, without saying it directly, it would be awesome.

Font styles to use
Sans Serif

Requirements
Must have
• I would like the testimonials to have a designated page (mentioned in the brief) but I would like the testimonials to be linked to the gallery page and when the picture are open of completed job the relevant testimonials would pop up near the pictures.

Nice to have
• I would like peolpe to understand that they are buy a price when they are getting quote to build there house. It seems like people just look for the cheapest price and end up with an inferior product. Where as people need to understand that a builder with the high price ( not astronomically higher 15-20% higher) are the ones with correct systems in place, a bide by correct OHS and use proper and correct product. If that can be conveyed through the website somehow, without saying it directly, it would be awesome.

```html
<!DOCTYPE html>
<html lang="en">
<head>
<meta charset="utf-8">
<title>Merrivale Construction — Luxury Custom Home Builder</title>
<link href="https://fonts.googleapis.com/css2?family=Cinzel:wght@700&family=Poppins:wght@600;700&family=Roboto:wght@400;500&family=Alegreya:ital@1&display=swap" rel="stylesheet">
<style>
:root{
  --blue:#1a73c1;
  --blue-dark:#145d9e;
  --ink:#111111;
  --text:#8a8a8a;
  --light:#f7f8fa;
  --line:#e6e8ec;
  --footer:#232323;
  --white:#ffffff;
}
*{margin:0;padding:0;box-sizing:border-box}
html,body{width:1200px;height:3450px;overflow:hidden}
body{font-family:'Roboto',Arial,sans-serif;color:var(--ink);background:var(--white);position:relative}
.abs{position:absolute}
.heading{font-family:'Cinzel',Georgia,serif;font-weight:700;font-variant:small-caps;color:var(--ink);letter-spacing:1px}
.heading span{color:var(--blue)}
.center{text-align:center;left:0;width:1200px}
.btn{display:flex;align-items:center;justify-content:space-between;background:var(--blue);color:var(--white);border-radius:24px;text-transform:uppercase;letter-spacing:.5px}
.btn .dot{width:30px;height:30px;border-radius:50%;background:var(--white);display:flex;align-items:center;justify-content:center}

/* hero */
.hero{left:0;top:0;width:1200px;height:690px;background:linear-gradient(160deg,#4a4f55 0%,#6b6a66 40%,#8a8276 70%,#5b5850 100%)}
.hero-shade{left:0;top:0;width:1200px;height:690px;background:rgba(20,25,35,.25)}
.brand{left:161px;top:27px;display:flex;align-items:center;gap:10px;color:var(--white);font-family:'Poppins',sans-serif;font-weight:700;font-size:18px;letter-spacing:1px}
.brand i{width:14px;height:14px;background:var(--blue);border-radius:50%;display:block}
.nav{left:422px;top:45px;display:flex;gap:22px;font-size:11.5px;color:var(--white);letter-spacing:.3px}
.nav a{color:inherit;text-decoration:none}
.nav a.active{color:var(--blue);border-bottom:2px solid var(--blue);padding-bottom:9px}
.phone{left:868px;top:31px;width:170px;height:44px;border-radius:22px;background:var(--blue);color:var(--white);display:flex;align-items:center;gap:14px;padding-left:5px;font-size:18px}
.phone .ring{width:34px;height:34px;border-radius:50%;background:var(--white);display:flex;align-items:center;justify-content:center}
.hero-title{top:226px;font-family:'Poppins',sans-serif;font-weight:700;font-size:44px;line-height:53px;color:var(--white);text-transform:uppercase;letter-spacing:1px;text-shadow:0 0 2px rgba(0,0,0,.4)}
.hero-sub{top:401px;font-size:14px;line-height:22px;color:var(--white)}

/* steps */
.step{width:82px;height:82px;border-radius:50%;background:var(--white);box-shadow:0 2px 8px rgba(0,0,0,.18);display:flex;align-items:center;justify-content:center;top:638px}
.step-label{top:744px;width:140px;text-align:center;font-weight:500;font-size:16px;letter-spacing:1px}

/* welcome */
.welcome-bg{left:0;top:690px;width:1200px;height:502px;background:var(--light)}
.welcome-title{left:162px;top:820px;font-size:34px;line-height:38px}
.para{font-size:11px;line-height:21px;color:var(--text)}
.welcome-mark{left:769px;top:825px;width:226px;height:307px;background:var(--blue);display:flex;align-items:center;justify-content:center;flex-direction:column;gap:14px;color:var(--white);font-family:'Roboto',sans-serif;font-weight:500;font-size:18px;text-align:center}
.welcome-mark i{width:60px;height:60px;border-radius:50%;border:4px solid var(--white);display:block}

/* services */
.card{top:1388px;width:271px;height:375px;background:#fbfbfc;border:1px solid #eeeeee}
.card .photo{width:269px;height:180px;position:relative;overflow:hidden}
.card .photo::before{content:"";position:absolute;left:0;top:0;border-top:100px solid var(--blue);border-right:100px solid transparent}
.card h3{font-weight:500;font-size:16px;letter-spacing:1px;margin:24px 0 0 23px}
.card p{margin:12px 20px 0 23px}
.card .btn{margin:18px 0 0 22px;width:120px;height:31px;padding:0 3px 0 13px;font-size:10px}
.card .btn .dot{width:25px;height:25px}

/* feedback */
.feedback-bg{left:0;top:1829px;width:1200px;height:288px;background:var(--light)}
.avatar{left:302px;top:1958px;width:96px;height:96px;border-radius:50%;border:3px solid var(--blue);background:linear-gradient(160deg,#b7c7d6,#7b8d9f)}
.quote{left:431px;top:1956px;width:480px;font-family:'Alegreya',Georgia,serif;font-style:italic;font-size:13px;line-height:22px;color:var(--text)}
.client{left:431px;top:2037px;font-size:13px;font-weight:500}

/* gallery */
.filters{top:2236px;font-size:12px;color:#555;letter-spacing:.5px}
.filters span{margin:0 14px}
.filters .on{color:var(--blue);text-decoration:underline}
.tile{background:#ccc}
.feature-tile{left:161px;top:2289px;width:202px;height:246px;background:var(--blue);color:var(--white);text-align:center}
.feature-tile i{display:block;width:64px;height:64px;border-radius:50%;border:5px solid var(--white);margin:40px auto 0}
.feature-tile h4{font-weight:500;font-size:13px;margin-top:44px;letter-spacing:.5px}
.feature-tile p{font-size:11px;line-height:20px;margin-top:8px}

/* newsletter */
.news-bg{left:0;top:2600px;width:1200px;height:268px;background:var(--light)}
.subscribe{left:346px;top:2763px;width:506px;height:42px;background:var(--white);border:1px solid var(--line);border-radius:21px;display:flex;align-items:center;padding-left:14px;gap:10px;font-size:11px;color:#999}
.subscribe .btn{position:absolute;right:0;top:3px;width:120px;height:36px;justify-content:center;font-size:13px;text-transform:none;letter-spacing:.3px}

/* footer */
.footer{left:0;top:2868px;width:1200px;height:472px;background:var(--footer)}
.foot-title{top:2926px;font-size:16px;color:var(--white)}
.rule{height:1px;background:#444}
.news-item{left:161px;width:226px;display:flex;gap:12px;align-items:flex-start}
.news-item .thumb{width:66px;height:66px;border-radius:50%;border:3px solid var(--blue);background:linear-gradient(150deg,#9aa6b2,#5e6b78);flex:none}
.news-item p{font-size:11.5px;line-height:19px;color:var(--white);margin-top:6px}
.news-item small{display:block;color:var(--blue);font-size:9.5px;margin-top:6px}
.form{left:440px;top:2983px;width:300px;height:292px;background:var(--white);border-radius:4px;padding:16px 15px}
.form p{font-size:10px;line-height:17px;color:#999}
.field{border:1px solid var(--line);background:#fbfbfb;height:33px;margin-top:11px;font-size:10px;color:#777;padding:10px 12px}
.field.tall{height:58px}
.form .btn{width:104px;height:36px;justify-content:center;margin-top:16px;font-size:12px}
.contact{left:796px;width:244px;display:flex;gap:12px}
.contact h5{color:var(--blue);font-weight:400;font-size:14px}
.contact p{color:var(--white);font-size:10.5px;line-height:18px;margin-top:4px}

/* bottom bar */
.bar{left:0;top:3340px;width:1200px;height:110px;background:var(--blue)}
.links{left:162px;top:3376px;font-size:11px;color:var(--white)}
.links span{margin:0 6px;opacity:.8}
.copy{left:162px;top:3402px;font-size:9px;color:#dce9f6}
.social{top:3374px;width:38px;height:38px;border-radius:50%;background:#2a2a2a}
</style>
</head>
<body>

<!-- Hero -->
<div class="abs hero" role="img" aria-label="Photo of builders in hard hats and safety vests walking across a construction site"></div>
<div class="abs hero-shade"></div>
<svg class="abs" style="left:0;top:560px" width="1200" height="140" viewBox="0 0 1200 140">
  <path d="M0 26 Q600 150 1200 26 L1200 140 L0 140 Z" fill="#f7f8fa"/>
  <path d="M0 26 Q600 150 1200 26" fill="none" stroke="#1a73c1" stroke-width="7"/>
</svg>

<div class="abs brand"><i></i>Merrivale Construction</div>
<nav class="abs nav">
  <a class="active">HOME</a><a>ABOUT US</a><a>SERVICES</a><a>GALLERY</a><a>TESTIMONIAL</a><a>CONTACT</a>
</nav>
<div class="abs phone">
  <span class="ring"><svg width="18" height="18" viewBox="0 0 24 24"><path d="M6.6 10.8c1.4 2.8 3.8 5.1 6.6 6.6l2.2-2.2c.3-.3.7-.4 1-.2 1.1.4 2.3.6 3.6.6.6 0 1 .4 1 1V20c0 .6-.4 1-1 1C10.6 21 3 13.4 3 4c0-.6.4-1 1-1h3.5c.6 0 1 .4 1 1 0 1.3.2 2.5.6 3.6.1.3 0 .7-.2 1L6.6 10.8z" fill="#111"/></svg></span>
  123.456.7890
</div>

<h1 class="abs center hero-title">A High End<br>Luxury Custom<br>Home Builder</h1>
<p class="abs center hero-sub">Lorem ipsum dolor sit amet, consectetur adipiscing elit, sed do eiusmod tempor<br>incididunt ut theye labore et dolore magna aliqua.</p>

<!-- Steps -->
<div class="abs step" style="left:385px">
  <svg width="48" height="42" viewBox="0 0 48 42"><rect x="2" y="2" width="44" height="32" rx="2" fill="none" stroke="#111" stroke-width="2"/><rect x="8" y="8" width="14" height="10" fill="#1a73c1"/><line x1="26" y1="10" x2="40" y2="10" stroke="#111" stroke-width="2"/><line x1="26" y1="16" x2="40" y2="16" stroke="#111" stroke-width="2"/><line x1="8" y1="26" x2="40" y2="26" stroke="#1a73c1" stroke-width="2"/><line x1="6" y1="38" x2="42" y2="38" stroke="#111" stroke-width="2"/></svg>
</div>
<div class="abs step" style="left:558px">
  <svg width="46" height="46" viewBox="0 0 46 46"><rect x="4" y="14" width="38" height="24" rx="2" fill="none" stroke="#111" stroke-width="2"/><line x1="23" y1="38" x2="23" y2="44" stroke="#111" stroke-width="2"/><line x1="14" y1="44" x2="32" y2="44" stroke="#111" stroke-width="2"/><line x1="14" y1="4" x2="34" y2="28" stroke="#1a73c1" stroke-width="4"/><line x1="34" y1="4" x2="14" y2="28" stroke="#111" stroke-width="2"/></svg>
</div>
<div class="abs step" style="left:731px">
  <svg width="46" height="48" viewBox="0 0 46 48"><line x1="30" y1="4" x2="30" y2="46" stroke="#111" stroke-width="2"/><line x1="10" y1="8" x2="44" y2="8" stroke="#111" stroke-width="2"/><rect x="26" y="10" width="8" height="34" fill="none" stroke="#1a73c1" stroke-width="2"/><path d="M4 30 L14 22 L24 30 L24 46 L4 46 Z" fill="#1a73c1"/><line x1="2" y1="46" x2="44" y2="46" stroke="#111" stroke-width="2"/></svg>
</div>
<div class="abs step-label" style="left:356px">PLAN</div>
<div class="abs step-label" style="left:529px">DESIGN</div>
<div class="abs step-label" style="left:702px">BUILD</div>

<!-- Welcome -->
<div class="abs welcome-bg" style="z-index:-1"></div>
<h2 class="abs heading welcome-title">Welcome To<br><span>Merrivale Construction</span></h2>
<p class="abs para" style="left:162px;top:912px;width:520px">Lorem ipsum dolor sit amet, consectetur adipiscing elit, sed do eiusmod tempor incididunt ut theye labore et dolore magna aliqua. Ut enim ad minim veniam, quis nostrud exercitation ullamco laboris nisi ut aliquip ex ea commodo consequat. Duis aute irure dolor in reprehenderit in voluptate velited esse cillum dolore eu fugiat nulla pariatur. Excepteur sint occaecat cupidatat non proident, sunt in culpa qui officia deserunt mollit anim id est laborum.</p>
<p class="abs para" style="left:162px;top:1027px;width:520px">Lorem ipsum dolor sit amet, consectetur adipiscing elit, sed do eiusmod tempor incididunt ut theye labore et dolore magna aliqua. Ut enim ad minim veniam, quis nostrud exercitation.</p>
<div class="abs btn" style="left:162px;top:1088px;width:172px;height:45px;padding:0 6px 0 18px;font-size:12.5px">More About Us<span class="dot" style="width:34px;height:34px"><svg width="14" height="14"><circle cx="7" cy="7" r="6" fill="#1a73c1"/></svg></span></div>
<div class="abs welcome-mark"><i></i>Merrivale<br>Construction</div>

<!-- Services -->
<h2 class="abs heading center" style="top:1248px;font-size:35px">Our <span>Services</span></h2>
<p class="abs center para" style="top:1309px;font-size:13px;line-height:23px">Lorem ipsum dolor sit amet, consectetur adipiscing elit, sed do eiusmod tempor<br>incididunt ut theye labore et dolore magna aliqua.</p>

<div class="abs card" style="left:161px">
  <div class="photo" role="img" aria-label="Photo of an engineer with a laptop on a building site" style="background:linear-gradient(150deg,#b9b1a0,#7d7564)"></div>
  <h3>PLAN</h3>
  <p class="para">Lorem ipsum dolor sit amet, consectetur adip scing elit, sed do eiusmod tempor incididunt ut labore et dolore magna aliqua.</p>
  <div class="btn">Learn More<span class="dot"><svg width="12" height="10"><path d="M0 5H10M6 1L10 5L6 9" fill="none" stroke="#111" stroke-width="1.5"/></svg></span></div>
</div>
<div class="abs card" style="left:465px">
  <div class="photo" role="img" aria-label="Photo of hands reviewing architectural plans on a desk" style="background:linear-gradient(150deg,#d4d6d8,#7c8087)"></div>
  <h3>DESIGN</h3>
  <p class="para">Lorem ipsum dolor sit amet, consectetur adip scing elit, sed do eiusmod tempor incididunt ut labore et dolore magna aliqua.</p>
  <div class="btn">Learn More<span class="dot"><svg width="12" height="10"><path d="M0 5H10M6 1L10 5L6 9" fill="none" stroke="#111" stroke-width="1.5"/></svg></span></div>
</div>
<div class="abs card" style="left:769px">
  <div class="photo" role="img" aria-label="Photo of two builders in hard hats working on a timber frame" style="background:linear-gradient(150deg,#8b95a2,#5a5548)"></div>
  <h3>BUILD</h3>
  <p class="para">Lorem ipsum dolor sit amet, consectetur adip scing elit, sed do eiusmod tempor incididunt ut labore et dolore magna aliqua.</p>
  <div class="btn">Learn More<span class="dot"><svg width="12" height="10"><path d="M0 5H10M6 1L10 5L6 9" fill="none" stroke="#111" stroke-width="1.5"/></svg></span></div>
</div>

<!-- Feedback -->
<div class="abs feedback-bg" style="z-index:-1"></div>
<h2 class="abs heading center" style="top:1887px;font-size:35px">Client's <span>Feedback</span></h2>
<svg class="abs" style="left:256px;top:1985px" width="16" height="40"><path d="M14 2L3 20L14 38" fill="none" stroke="#1a73c1" stroke-width="2"/></svg>
<svg class="abs" style="left:930px;top:1985px" width="16" height="40"><path d="M2 2L13 20L2 38" fill="none" stroke="#999" stroke-width="1.5"/></svg>
<div class="abs avatar" role="img" aria-label="Portrait of a satisfied client"></div>
<p class="abs quote">Lorem ipsum dolor sit amet, consectetur adipiscing elit, sed do eiusmod tempor incididunt ut labore et dolore magna aliqua. Ut enim ad minim veniam, quis nostrud exercitation ullamco laboris.</p>
<p class="abs client">-&nbsp; Client's Name</p>

<!-- Gallery -->
<h2 class="abs heading center" style="top:2170px;font-size:35px">Our <span>Gallery</span></h2>
<p class="abs center filters"><span class="on">ALL</span>|<span>COMMERCIAL</span>|<span>RESIDENTIAL</span>|<span>OTHERS</span></p>

<div class="abs feature-tile"><i></i><h4>LOREM IPSUM</h4><p>Lorem ipsum dolor sit amet,<br>consectetur adipscing elit.</p></div>
<div class="abs tile" role="img" aria-label="Photo of a living room with a grey sofa" style="left:386px;top:2289px;width:158px;height:112px;background:linear-gradient(160deg,#d9d6d0,#8d8a84)"></div>
<div class="abs tile" role="img" aria-label="Photo of a modern house among trees" style="left:386px;top:2424px;width:158px;height:111px;background:linear-gradient(160deg,#6f8c58,#3f4a3c)"></div>
<div class="abs tile" role="img" aria-label="Photo of a white two-storey luxury home" style="left:567px;top:2289px;width:292px;height:134px;background:linear-gradient(180deg,#a9c3de,#d8dcd9 60%,#7e8f6a)"></div>
<div class="abs tile" role="img" aria-label="Photo of a bright room with a plant" style="left:567px;top:2446px;width:134px;height:99px;background:linear-gradient(160deg,#f1ece4,#c8b8a0)"></div>
<div class="abs tile" role="img" aria-label="Photo of a living room with timber furniture" style="left:724px;top:2446px;width:135px;height:89px;background:linear-gradient(160deg,#d4d4d2,#7e6c58)"></div>
<div class="abs tile" role="img" aria-label="Photo of a bathroom vanity" style="left:882px;top:2289px;width:158px;height:112px;background:linear-gradient(160deg,#d9cbb6,#6b4a33)"></div>
<div class="abs tile" role="img" aria-label="Photo of an open-plan lounge" style="left:882px;top:2424px;width:158px;height:111px;background:linear-gradient(160deg,#c9c2b6,#6a5a48)"></div>

<!-- Newsletter -->
<div class="abs news-bg" style="z-index:-1"></div>
<h2 class="abs heading center" style="top:2651px;font-size:35px">Stay Tuned <span>With Us</span></h2>
<p class="abs center para" style="top:2714px">Subcribe now and receive monthly projects and newsletter with Merrivale Construction</p>
<div class="abs subscribe">
  <svg width="16" height="12"><rect x="1" y="1" width="14" height="10" fill="none" stroke="#1a73c1"/><path d="M1 1L8 7L15 1" fill="none" stroke="#1a73c1"/></svg>
  Enter Email....
  <div class="btn">Subcribe Now</div>
</div>

<!-- Footer -->
<div class="abs footer"></div>
<h4 class="abs heading foot-title" style="left:163px;color:#fff">Recent <span>News Updates</span></h4>
<h4 class="abs heading foot-title" style="left:442px;color:#fff">Send <span>Message</span></h4>
<h4 class="abs heading foot-title" style="left:797px;color:#fff">Get In <span>Touch</span></h4>

<div class="abs rule" style="left:161px;top:2984px;width:226px"></div>
<div class="abs news-item" style="top:2995px"><div class="thumb" role="img" aria-label="Photo from a project build"></div><p>Lorem ipsum dconsectetur dolore magna aliqua.<small>25 June 2020</small></p></div>
<div class="abs rule" style="left:161px;top:3081px;width:226px"></div>
<div class="abs news-item" style="top:3092px"><div class="thumb" role="img" aria-label="Photo of a builder on site"></div><p>Lorem ipsum dconsectetur dolore magna aliqua.<small>25 June 2020</small></p></div>
<div class="abs rule" style="left:161px;top:3178px;width:226px"></div>
<div class="abs news-item" style="top:3189px"><div class="thumb" role="img" aria-label="Photo of framing work"></div><p>Lorem ipsum dconsectetur dolore magna aliqua.<small>25 June 2020</small></p></div>
<div class="abs rule" style="left:161px;top:3276px;width:226px"></div>

<div class="abs form">
  <p>Lorem ipsum dconsectetur adipiscing&nbsp; ut labore et dolore magna aliqua.</p>
  <div class="field">Name</div>
  <div class="field">Email</div>
  <div class="field tall">Message / comments :</div>
  <div class="btn">Send Now</div>
</div>

<div class="abs rule" style="left:796px;top:2984px;width:244px"></div>
<div class="abs contact" style="top:3004px">
  <svg width="26" height="24" viewBox="0 0 26 24"><path d="M13 2L1 12H5V22H11V15H15V22H21V12H25Z" fill="#1a73c1"/></svg>
  <div><h5>Merrivale Construction</h5><p>123,Address,State Name, Street<br>Name, City Name, Zipcode</p></div>
</div>
<div class="abs rule" style="left:796px;top:3080px;width:244px"></div>
<div class="abs contact" style="top:3106px">
  <svg width="26" height="26" viewBox="0 0 24 24"><path d="M6.6 10.8c1.4 2.8 3.8 5.1 6.6 6.6l2.2-2.2c.3-.3.7-.4 1-.2 1.1.4 2.3.6 3.6.6.6 0 1 .4 1 1V20c0 .6-.4 1-1 1C10.6 21 3 13.4 3 4c0-.6.4-1 1-1h3.5c.6 0 1 .4 1 1 0 1.3.2 2.5.6 3.6.1.3 0 .7-.2 1L6.6 10.8z" fill="#1a73c1"/></svg>
  <div><h5>Phone</h5><p>123.456.7890</p></div>
</div>
<div class="abs rule" style="left:796px;top:3178px;width:244px"></div>
<div class="abs contact" style="top:3204px">
  <svg width="26" height="20" viewBox="0 0 26 20"><rect x="1" y="1" width="24" height="18" fill="#1a73c1"/><path d="M1 1L13 11L25 1" fill="none" stroke="#232323" stroke-width="2"/></svg>
  <div><h5>Email</h5><p>info@merrivaleconstruction.com</p></div>
</div>
<div class="abs rule" style="left:796px;top:3276px;width:244px"></div>

<!-- Bottom bar -->
<div class="abs bar"></div>
<p class="abs links">Home<span>|</span>About Us<span>|</span>Services<span>|</span>Gallery<span>|</span>Testimonials<span>|</span>Contact Us</p>
<p class="abs copy">© Merrivale Construction - 2020 . All Rights Reserved</p>
<div class="abs social" style="left:878px" aria-label="Social link"></div>
<div class="abs social" style="left:920px" aria-label="Social link"></div>
<div class="abs social" style="left:961px" aria-label="Social link"></div>
<div class="abs social" style="left:1002px" aria-label="Social link"></div>

</body>
</html>
```